" Atendimento individual, observando as necessidades do aluno com especial atenção às lacunas de conhecimento (conteúdos que não foram aprendidos/absorvidos adequadamente e que dificultam a compreensão de novos tópicos). Para tanto, preparamos aulas exclusivas para cada aluno, que é sempre visto como um indivíduo independente que devem ter suas necessidades respeitadas. Dessa forma, trabalhamos para estimular conhecimento, criatividade e autonomia, para vencer dificuldades, enfrentar desafios e formar organização pessoal através de um horário fixo de estudos. "

```html
<!DOCTYPE html>
<html lang="pt-BR">
<head>
<meta charset="utf-8">
<title>Clara Moreira — Papel Timbrado</title>
<link rel="stylesheet" href="https://fonts.googleapis.com/css2?family=Montserrat:wght@400;500&display=swap">
<style>
  :root {
    --backdrop: #e4e4e4;
    --paper: #ffffff;
    --brand: #8a4a32;
    --brand-soft: #b57a63;
    --ink: #4a4a4a;
    --ink-light: #777777;
    --rule: #c9c9c9;
    --watermark: #f1f1f1;
  }
  * { margin: 0; padding: 0; box-sizing: border-box; }
  html, body {
    width: 1200px; height: 1200px; overflow: hidden;
    background: var(--backdrop);
    font-family: "Montserrat", sans-serif;
  }
  .letterhead {
    position: absolute; left: 190px; top: 40px;
    width: 820px; height: 1120px;
    background: var(--paper);
    box-shadow: 0 6px 24px rgba(0,0,0,0.12);
    overflow: hidden;
  }
  .letterhead__tab {
    position: absolute; top: 0; left: 310px;
    width: 200px; height: 10px;
    background: var(--brand);
  }
  .letterhead__watermark {
    position: absolute; left: -120px; top: 260px;
    width: 560px; height: 620px;
    background: radial-gradient(ellipse at 40% 50%, var(--watermark) 0%, rgba(241,241,241,0) 70%);
  }
  .brand {
    position: absolute; top: 52px; left: 0; right: 0;
    display: flex; justify-content: center; align-items: center; gap: 12px;
  }
  .brand__dot {
    width: 16px; height: 16px; border-radius: 50%;
    background: var(--brand);
  }
  .brand__name {
    font-weight: 500; font-size: 30px; letter-spacing: 2px;
    text-transform: uppercase; color: var(--brand);
  }
  .letter {
    position: absolute; top: 180px; left: 90px; width: 620px;
    font-size: 14px; line-height: 1.55; color: var(--ink);
  }
  .letter p { margin-bottom: 24px; }
  .signature {
    position: absolute; top: 700px; left: 90px; right: 90px;
  }
  .signature__mark {
    position: absolute; right: 40px; top: 0;
    width: 150px; height: 56px;
    background: linear-gradient(90deg, rgba(60,60,60,0.05), rgba(60,60,60,0.14), rgba(60,60,60,0.05));
  }
  .signature__line {
    position: absolute; top: 62px; left: 280px; right: 0;
    height: 1px; background: var(--rule);
  }
  .footer {
    position: absolute; bottom: 60px; left: 70px; right: 70px;
    text-align: center; color: var(--ink-light);
    font-size: 13px; line-height: 1.6;
  }
  .footer__rule {
    height: 2px; background: var(--brand-soft); margin-bottom: 14px;
  }
</style>
</head>
<body>
  <main class="letterhead">
    <div class="letterhead__tab"></div>
    <div class="letterhead__watermark" role="img" aria-label="Faint brand decoration"></div>

    <header class="brand">
      <span class="brand__dot"></span>
      <span class="brand__name">Clara Moreira</span>
    </header>

    <section class="letter">
      <p>Prezada família,</p>
      <p>Agradecemos o contato e apresentamos nossa proposta de aulas particulares, pensada para cada aluno e suas lacunas de conhecimento.</p>
      <p>As aulas são exclusivas e seguem um horário fixo de estudos.</p>
      <p>Seguimos à disposição para conversar.</p>
      <p>Atenciosamente,</p>
    </section>

    <div class="signature">
      <div class="signature__mark" role="img" aria-label="Handwritten signature"></div>
      <div class="signature__line"></div>
    </div>

    <footer class="footer">
      <div class="footer__rule"></div>
      <div>+ 00-00 0000-0000 &nbsp; + 00-00 0000-0000</div>
      <div>email@exemplo.com &nbsp;&nbsp; www.site.com.br</div>
      <div>Endereço Completo | Rua | Nº | Bairro | Cidade | CEP | UF | Brasil</div>
    </footer>
  </main>
</body>
</html>
```